Stationery Design Project - Dalgren-Fairweather

Letterhead
Size: A4 - 210mm x 297mm

With Compliments Slip
Size: DL - 210mm x 99mm

Notepad
Size: 250mm x 140mm

Presentation Folder
Size: A4

-
Dalgren-Fairweather Executive Search & Consulting
*Perth *Brisbane *Seoul *Hongkong

Website to be: www.dalgrenfairweather.com.au

Head Hunting & Recruitment Agency

Area we recruit in:
Executive & General Management
Government & Public Sector
Executive Contracting
Accounting
Banking & Financial Services
Information Technology & Telecommunications
Legal
Operations, Engineering & Construction
Human Resources
Board Appointments

Please note we love the business card design so if we can keep that design inline that would be great.

Best of luck

Lionel

```html
<!DOCTYPE html>
<html lang="en">
<head>
<meta charset="utf-8">
<title>Dalgren-Fairweather – With Compliments Slip</title>
<link rel="stylesheet" href="https://fonts.googleapis.com/css2?family=Cinzel:wght@400&family=Open+Sans:wght@300;400;600&display=swap">
<style>
  :root {
    --backdrop: #e9e9ea;
    --paper: #f7f7f8;
    --ink: #2f3136;
    --ink-soft: #5b5e64;
    --band-dark: #2c2f36;
    --band-mid: #6b6f78;
    --band-light: #b9bcc2;
    --mark: #9a9da3;
  }
  * { margin: 0; padding: 0; box-sizing: border-box; }
  html, body {
    width: 1200px; height: 885px; overflow: hidden;
    background: var(--backdrop);
  }
  .slip {
    position: absolute;
    left: 100px; top: 207px;
    width: 1000px; height: 471px;
    background: var(--paper);
    box-shadow: 0 10px 30px rgba(0,0,0,0.12);
    font-family: "Open Sans", Arial, sans-serif;
    color: var(--ink);
  }
  .brand {
    position: absolute; left: 44px; top: 40px;
    display: flex; align-items: center; gap: 14px;
  }
  .brand__square {
    width: 34px; height: 34px; background: var(--mark);
  }
  .brand__name {
    font-family: "Cinzel", Georgia, serif;
    font-size: 21px; letter-spacing: 1px; color: var(--ink-soft);
    line-height: 1.1;
  }
  .brand__tagline {
    font-family: "Cinzel", Georgia, serif;
    font-size: 10.5px; letter-spacing: 1.2px; color: var(--ink-soft);
  }
  .sender {
    position: absolute; left: 44px; top: 232px;
    font-size: 10.5px; line-height: 1.5;
  }
  .sender__name { font-weight: 600; font-size: 12px; }
  .sender__role { color: var(--ink-soft); margin-bottom: 10px; }
  .sender__address { color: var(--ink-soft); margin-bottom: 8px; }
  .contacts {
    display: grid; grid-template-columns: auto auto;
    column-gap: 22px; row-gap: 3px; color: var(--ink-soft);
  }
  .contacts__item { display: flex; align-items: center; gap: 6px; }
  .contacts__item svg { width: 12px; height: 12px; flex: none; }
  .greeting {
    position: absolute; right: 60px; top: 196px;
    font-weight: 300; font-size: 40px; color: var(--ink);
  }
  .band {
    position: absolute; left: 0; right: 0; bottom: 28px; height: 22px;
    background: linear-gradient(90deg, var(--band-dark) 0%, var(--band-mid) 45%, var(--band-light) 62%, var(--band-mid) 80%, var(--band-dark) 100%);
  }
</style>
</head>
<body>
  <main class="slip">
    <header class="brand">
      <div class="brand__square"></div>
      <div>
        <div class="brand__name">Dalgren-Fairweather</div>
        <div class="brand__tagline">Executive Search &amp; Consulting</div>
      </div>
    </header>

    <section class="sender">
      <div class="sender__name">Maren J. Colby</div>
      <div class="sender__role">President</div>
      <div class="sender__address">
        Level 4, 18 Harlow Lane, Suite 310, P.O. Box WA 6000<br>
        EAST PERTH WA 6004, Australia
      </div>
      <div class="contacts">
        <div class="contacts__item">
          <svg viewBox="0 0 12 12"><circle cx="6" cy="6" r="6" fill="#5b5e64"/><path d="M3.5 3.2h1.4l.6 1.5-.8.6a4 4 0 0 0 2 2l.6-.8 1.5.6v1.4c-3 .3-5.6-2.3-5.3-5.3z" fill="#f7f7f8"/></svg>
          08 5550 1820
        </div>
        <div class="contacts__item">
          <svg viewBox="0 0 12 12"><circle cx="6" cy="6" r="6" fill="#5b5e64"/><circle cx="6" cy="6" r="2.2" fill="none" stroke="#f7f7f8" stroke-width="1"/><path d="M8.2 6v.9a1 1 0 0 0 1.3.5" fill="none" stroke="#f7f7f8" stroke-width="1"/></svg>
          mc@dalgrenfairweather.com.au
        </div>
        <div class="contacts__item">
          <svg viewBox="0 0 12 12"><circle cx="6" cy="6" r="6" fill="#5b5e64"/><rect x="3" y="4.5" width="6" height="4" fill="#f7f7f8"/><rect x="4" y="3" width="4" height="1.5" fill="#f7f7f8"/></svg>
          08 5550 1821
        </div>
        <div class="contacts__item">
          <svg viewBox="0 0 12 12"><circle cx="6" cy="6" r="6" fill="#5b5e64"/><circle cx="6" cy="6" r="3.2" fill="none" stroke="#f7f7f8" stroke-width=".9"/><path d="M2.8 6h6.4M6 2.8c-1.6 2-1.6 4.4 0 6.4M6 2.8c1.6 2 1.6 4.4 0 6.4" fill="none" stroke="#f7f7f8" stroke-width=".8"/></svg>
          www.dalgrenfairweather.com.au
        </div>
      </div>
    </section>

    <h1 class="greeting">With Best Compliments</h1>

    <div class="band"></div>
  </main>
</body>
</html>
```